Convert this PSD to vector, first one wins

I am having a hell of a time figuring out how to do this, and I have too much going on right now. I need help.

Needs to be Illustrator EPS. It is all white lettering accept for the top logo. No background.

```html
<!DOCTYPE html>
<html lang="en">
<head>
<meta charset="utf-8">
<title>The Lark Residence – Sales Center</title>
<link rel="stylesheet" href="https://fonts.googleapis.com/css2?family=Open+Sans:wght@400;600&display=swap">
<style>
  :root {
    --ink: #221f20;
    --paper: #ffffff;
    --stone: #a6a79a;
  }
  html, body {
    margin: 0;
    padding: 0;
    width: 829px;
    height: 1200px;
    overflow: hidden;
    background: var(--ink);
  }
  .sign {
    position: relative;
    width: 829px;
    height: 1200px;
    background: var(--ink);
    color: var(--paper);
    font-family: "Open Sans", Arial, sans-serif;
    font-weight: 400;
  }
  .line {
    position: absolute;
    left: 0;
    width: 100%;
    margin: 0;
    text-align: center;
    line-height: 1;
    white-space: nowrap;
  }
  .project-name {
    top: 88px;
    font-size: 36px;
    letter-spacing: 0.12em;
    color: var(--stone);
  }
  .center-title { top: 193px; font-size: 39px; letter-spacing: 0.2em; }
  .center-address { top: 243px; font-size: 29px; letter-spacing: 0.02em; }
  .day { font-size: 28px; letter-spacing: 0.2em; }
  .hours { font-size: 24px; letter-spacing: 0.17em; }
  .weekdays { top: 350px; }
  .weekday-hours { top: 386px; }
  .sunday { top: 457px; }
  .sunday-hours { top: 493px; }
  .rule {
    position: absolute;
    left: 281px;
    width: 257px;
    height: 2px;
    background: var(--paper);
  }
  .rule-top { top: 333px; }
  .rule-bottom { top: 540px; }
  .appointment { top: 597px; font-size: 25px; letter-spacing: 0.2em; }
  .phone { top: 634px; font-size: 25px; letter-spacing: 0.2em; }
  .brokerage { top: 966px; font-size: 30px; letter-spacing: 0.1em; }
  .website { top: 1085px; font-size: 26px; letter-spacing: 0.2em; }
</style>
</head>
<body>
  <main class="sign">
    <h1 class="line project-name">THE LARK RESIDENCE</h1>

    <h2 class="line center-title">SALES CENTER</h2>
    <p class="line center-address">240 WEST HARBOR STREET</p>

    <div class="rule rule-top"></div>
    <p class="line day weekdays">WEEKDAYS</p>
    <p class="line hours weekday-hours">11:00 AM - 6:00 PM</p>
    <p class="line day sunday">SUNDAY</p>
    <p class="line hours sunday-hours">1:00 PM - 3:00 PM</p>
    <div class="rule rule-bottom"></div>

    <p class="line appointment">BY APPOINTMENT</p>
    <p class="line phone">(555) 014-7720</p>

    <p class="line brokerage">NORTHGATE REALTY</p>

    <p class="line website">LARKRESIDENCE.ORG</p>
  </main>
</body>
</html>
```